Project Meridel PowerPoint Design

This is a PPT design for Power & Utilities company who are in the process of a technology upgrade for their Finance department. We are looking to develop a branded PPT for Project Meridel (specifically MERIDEL). Why does Meridel resonate? "The Earth is pointed almost directly at Meridel. During the course of the night,
Meridel does not rise or set, but remains in nearly the same spot above the
northern horizon year- round while the other stars circle around it."
Meridel represents the guiding principles that manage, monitor and
control the organizations financials.

Target Market(s)

Finance stakeholders impacted by technology enhancement

Font styles to use
Serif
Other font styles liked:
• Arial

Colors
0054AA
0677BA
7BADD7
CADEEF
E8F1F8

Requirements
Must have
• Various slide layout ( Cover slide, content slide, divider, etc). Attached is the logo and corporate colors
Nice to have
• Over the top creativity

```html
<!DOCTYPE html>
<html lang="en">
<head>
<meta charset="utf-8">
<title>Project Meridel – Presentation Template</title>
<link rel="stylesheet" href="https://fonts.googleapis.com/css2?family=Montserrat:wght@400;500;600;700&display=swap">
<style>
:root{
  --deep:#0054AA;
  --mid:#0677BA;
  --soft:#7BADD7;
  --pale:#CADEEF;
  --mist:#E8F1F8;
  --arc:#2450B4;
  --ink:#1a1a1a;
  --night:#0c111d;
  --stage:#f1f1f1;
  --board:#d4d4d6;
}
*{margin:0;padding:0;box-sizing:border-box}
html,body{width:1200px;height:2575px;overflow:hidden}
body{position:relative;background:var(--board);font-family:"Montserrat",Arial,sans-serif;color:var(--ink)}
.hero-stage{position:absolute;left:0;top:0;width:1200px;height:590px;background:var(--stage)}
.slide{position:absolute;width:540px;height:303px;overflow:hidden;background:#fff}
.fill{position:absolute;inset:0}
.photo{position:absolute}
.crescent{position:absolute;left:0;top:0;width:540px;height:282px}
.crescent path{fill:var(--arc)}
.logo{position:absolute;font-weight:600;color:var(--deep);letter-spacing:.08em;white-space:nowrap}
.logo--cover{left:45px;top:50px;font-size:17px}
.cover-title{position:absolute;left:45px;top:112px;font-size:30px;line-height:34px;font-weight:600;color:#fff}
.cover-sub{position:absolute;left:45px;top:180px;font-size:13px;color:var(--deep)}
.date-pill{position:absolute;left:45px;top:213px;width:153px;height:22px;border-radius:11px;background:var(--deep);color:#fff;font-size:6.5px;font-weight:700;text-align:center;line-height:22px}
.legal{position:absolute;left:0;bottom:0;width:540px;height:21px;background:#fff;font-size:5.5px;text-align:center;line-height:21px;color:#333}
.legal span{color:var(--deep)}
.cover--light .fill{background:linear-gradient(90deg,#fff 0%,#f4f7fb 50%,#c8d3e2 100%)}
.cover--light .cover-title{color:var(--ink)}
.cover--light .legal{background:var(--soft);color:#fff}
.cover--light .legal span{color:var(--deep)}
.cover--blue .fill{background:linear-gradient(90deg,#6f9fd9 0%,#82ade0 55%,#a9c4e6 100%)}
.cover--dark .fill{background:linear-gradient(90deg,#070a12 0%,#121a2b 55%,#26324a 100%)}
.cover--dark .date-pill{background:var(--soft)}
.photo--right{left:350px;top:0;width:190px;height:282px;opacity:.55}
.slide-title{position:absolute;left:0;width:540px;top:24px;text-align:center;font-size:20px;font-weight:500}
.slide-sub{position:absolute;left:0;width:540px;top:51px;text-align:center;font-size:9.5px;color:var(--mid)}
.bar-footer{position:absolute;left:0;bottom:0;width:540px;height:22px;background:var(--soft)}
.logo--footer{left:8px;bottom:4px;font-size:9px}
.page-arc{position:absolute;left:0;top:0;width:540px;height:303px}
.page-arc path{fill:var(--arc)}
.page-no{position:absolute;right:14px;bottom:6px;font-size:7px;color:#fff}
.toc-no{position:absolute;font-size:19px;color:#9aa3ad;font-weight:300;width:20px;text-align:center}
.toc-item{position:absolute;width:165px;padding-left:10px;border-left:1px solid #d7dde4}
.item-title{font-size:12px;font-weight:500;color:var(--deep);line-height:14px}
.small{font-size:6.5px;line-height:7.5px;color:#333}
.bullets{list-style:none}
.bullets li{position:relative;padding-left:12px;font-size:6.5px;line-height:7.5px;color:#333;margin-bottom:4px}
.bullets li::before{content:"";position:absolute;left:2px;top:2.5px;width:3px;height:3px;border-radius:50%;background:var(--deep)}
.split-title{position:absolute;left:300px;width:217px;top:58px;text-align:center;font-size:17px;line-height:19px;font-weight:500}
.split-text{position:absolute;left:308px;width:200px;top:112px;text-align:center;font-size:7.5px;line-height:8.6px;color:#333}
.legend-item{position:absolute;left:328px;width:180px}
.legend-item .item-title{font-size:10px;padding-left:20px;position:relative}
.legend-item .item-title::before{content:"";position:absolute;left:0;top:2px;width:11px;height:11px;background:var(--deep)}
.legend-item .small{padding-left:20px;margin-top:4px}
.grid-table{position:absolute;left:30px;top:80px;width:478px;border-collapse:collapse;font-size:6px}
.grid-table th{height:23px;background:var(--soft);color:#fff;font-weight:500;font-size:9px;border-right:1px solid #fff}
.grid-table th:first-child{background:var(--deep);text-align:left;padding-left:5px;font-weight:700}
.grid-table td{height:16.8px;text-align:center;background:#fafafa;border-bottom:1px solid #e4e4e4}
.grid-table td:first-child{text-align:left;padding-left:5px}
.contact-head{position:absolute;left:45px;top:166px;color:#fff;font-size:12px;font-weight:500}
.contact-list{position:absolute;left:45px;top:192px;list-style:none}
.contact-list li{display:flex;align-items:center;gap:8px;color:#fff;font-size:7px;height:16px}
.contact-list svg{width:10px;height:10px;fill:none;stroke:#fff;stroke-width:1.4}
</style>
</head>
<body>

<div class="hero-stage"></div>

<!-- Hero cover shown flat -->
<section class="slide cover--blue" style="left:330px;top:140px">
  <div class="fill"></div>
  <div class="photo photo--right" role="img" aria-label="Photo of a desk meeting with coffee and tablet, blue tinted" style="background:linear-gradient(180deg,#c3d4ea,#9ebbe0)"></div>
  <svg class="crescent" viewBox="0 0 540 282"><path d="M392 0 A200 200 0 0 0 505 285 A230 230 0 0 1 350 0 Z"/></svg>
  <p class="logo logo--cover">PROJECT MERIDEL</p>
  <h1 class="cover-title">Presentation<br>Title Goes Here!</h1>
  <p class="cover-sub">Subtitle of Presentation Goes Here!</p>
  <p class="date-pill">Thursday, November 11, 2021</p>
  <footer class="legal">© 2020 <span>Project-Meridel</span> | All Rights Reserved.</footer>
</section>

<!-- 1 Cover blue -->
<section class="slide cover--blue" style="left:51px;top:610px">
  <div class="fill"></div>
  <div class="photo photo--right" role="img" aria-label="Photo of a desk meeting with coffee and tablet, blue tinted" style="background:linear-gradient(180deg,#c3d4ea,#9ebbe0)"></div>
  <svg class="crescent" viewBox="0 0 540 282"><path d="M392 0 A200 200 0 0 0 505 285 A230 230 0 0 1 350 0 Z"/></svg>
  <p class="logo logo--cover">PROJECT MERIDEL</p>
  <h2 class="cover-title">Presentation<br>Title Goes Here!</h2>
  <p class="cover-sub">Subtitle of Presentation Goes Here!</p>
  <p class="date-pill">Thursday, November 11, 2021</p>
  <footer class="legal">© 2020 <span>Project-Meridel</span> | All Rights Reserved.</footer>
</section>

<!-- 2 Cover light -->
<section class="slide cover--light" style="left:609px;top:610px">
  <div class="fill"></div>
  <div class="photo photo--right" role="img" aria-label="Photo of colleagues shaking hands over a laptop, faded" style="background:linear-gradient(180deg,#dfe5ee,#b9c4d4)"></div>
  <svg class="crescent" viewBox="0 0 540 282"><path d="M392 0 A200 200 0 0 0 505 285 A230 230 0 0 1 350 0 Z"/></svg>
  <p class="logo logo--cover">PROJECT MERIDEL</p>
  <h2 class="cover-title">Presentation<br>Title Goes Here!</h2>
  <p class="cover-sub">Subtitle of Presentation Goes Here!</p>
  <p class="date-pill">Thursday, November 11, 2021</p>
  <footer class="legal">© 2020 <span>Project-Meridel</span> | All Rights Reserved.</footer>
</section>

<!-- 3 Cover dark -->
<section class="slide cover--dark" style="left:51px;top:932px">
  <div class="fill"></div>
  <div class="photo photo--right" role="img" aria-label="Dark photo of hands working on a laptop with papers" style="background:linear-gradient(180deg,#2b3548,#3c4a63)"></div>
  <svg class="crescent" viewBox="0 0 540 282"><path d="M392 0 A200 200 0 0 0 505 285 A230 230 0 0 1 350 0 Z"/></svg>
  <p class="logo logo--cover">PROJECT MERIDEL</p>
  <h2 class="cover-title">Presentation<br>Title Goes Here!</h2>
  <p class="cover-sub">Subtitle of Presentation Goes Here!</p>
  <p class="date-pill">Thursday, November 11, 2021</p>
  <footer class="legal">© 2020 <span>Project-Meridel</span> | All Rights Reserved.</footer>
</section>

<!-- 4 Table of contents -->
<section class="slide" style="left:609px;top:932px">
  <h2 class="slide-title">Table of Contents</h2>
  <p class="slide-sub">Slide subtitle Goes Here</p>
  <span class="toc-no" style="left:69px;top:104px">1</span>
  <div class="toc-item" style="left:93px;top:100px"><p class="item-title">Title Goes Here</p><p class="small">Lorem ipsum dolor sit amet, consectetur adipiscing elit. Vivamus eu dui ex.</p></div>
  <span class="toc-no" style="left:282px;top:104px">2</span>
  <div class="toc-item" style="left:306px;top:100px"><p class="item-title">Title Goes Here</p><p class="small">Lorem ipsum dolor sit amet, consectetur adipiscing elit. Vivamus eu dui ex.</p></div>
  <span class="toc-no" style="left:69px;top:157px">3</span>
  <div class="toc-item" style="left:93px;top:153px"><p class="item-title">Title Goes Here</p><p class="small">Lorem ipsum dolor sit amet, consectetur adipiscing elit. Vivamus eu dui ex.</p></div>
  <span class="toc-no" style="left:282px;top:157px">4</span>
  <div class="toc-item" style="left:306px;top:153px"><p class="item-title">Title Goes Here</p><p class="small">Lorem ipsum dolor sit amet, consectetur adipiscing elit. Vivamus eu dui ex.</p></div>
  <span class="toc-no" style="left:69px;top:210px">5</span>
  <div class="toc-item" style="left:93px;top:206px"><p class="item-title">Title Goes Here</p><p class="small">Lorem ipsum dolor sit amet, consectetur adipiscing elit. Vivamus eu dui ex.</p></div>
  <span class="toc-no" style="left:282px;top:210px">6</span>
  <div class="toc-item" style="left:306px;top:206px"><p class="item-title">Title Goes Here</p><p class="small">Lorem ipsum dolor sit amet, consectetur adipiscing elit. Vivamus eu dui ex.</p></div>
  <div class="bar-footer"></div>
  <p class="logo logo--footer">MERIDEL</p>
  <svg class="page-arc" viewBox="0 0 540 303"><path d="M481 303 A62 40 0 0 1 540 270 L540 278 A55 34 0 0 0 493 303 Z"/></svg>
  <span class="page-no">4</span>
</section>

<!-- 5 Image + text -->
<section class="slide" style="left:51px;top:1253px">
  <div class="photo" role="img" aria-label="Photo of a hand with a pen over printed bar charts" style="left:23px;top:23px;width:263px;height:235px;background:linear-gradient(135deg,#e6e9ee,#f7f8fa 55%,#dfe4ec)"></div>
  <h2 class="split-title">Slide Title<br>Goes Here</h2>
  <p class="split-text">Lorem ipsum dolor sit amet, consectetur adipiscing elit. Vivamus eu dui ex. Curabitur dapibus dignissim dui, in molestie metus feugiat sed. Praesent aliquet lorem ex, eu dapibus odio varius at. Duis eget tellus porta, consequat lacus vitae, venenatis dolor. Nulla facilisi. In et sollicitudin lacus. Donec risus orci, gravida sit amet risus vehicula. Lorem ipsum dolor sit amet, consectetur adipiscing elit. Vivamus eu dui ex.</p>
  <div class="bar-footer"></div>
  <p class="logo logo--footer">MERIDEL</p>
  <svg class="page-arc" viewBox="0 0 540 303"><path d="M481 303 A62 40 0 0 1 540 270 L540 278 A55 34 0 0 0 493 303 Z"/></svg>
  <span class="page-no">5</span>
</section>

<!-- 6 Image + bullets -->
<section class="slide" style="left:609px;top:1253px">
  <h2 class="slide-title">Slide Title Goes Here</h2>
  <p class="slide-sub">Subtitle of Slide Goes Here</p>
  <div class="photo" role="img" aria-label="Photo of a tablet showing a stock chart during a meeting" style="left:25px;top:92px;width:240px;height:157px;background:linear-gradient(135deg,#3a4350,#8a939f 60%,#c9ced6)"></div>
  <p class="item-title" style="position:absolute;left:282px;top:92px">Title Goes Here</p>
  <ul class="bullets" style="position:absolute;left:282px;top:112px;width:230px">
    <li>Lorem ipsum dolor sit amet, consectetur adipiscing elit. Vivamus eu dui ex. Curabitur dapibus dignissim dui, in molestie metus feugiat sed.</li>
    <li>Praesent aliquet lorem ex, eu dapibus odio varius at. Duis eget tellus porta, consequat lacus vitae, venenatis dolor.</li>
    <li>Nulla facilisi. In et sollicitudin lacus. Donec risus orci, gravida sit amet risus vehicula, aliquet pretium sapien. Nullam sit amet magna non ex bibendum mollis.</li>
    <li>Nunc vel neque eu augue dignissim congue ut vitae magna. Phasellus eget commodo arcu.</li>
    <li>Nunc vitae semper dui. Integer venenatis, tellus sit amet interdum pretium.</li>
  </ul>
  <div class="bar-footer"></div>
  <p class="logo logo--footer">MERIDEL</p>
  <svg class="page-arc" viewBox="0 0 540 303"><path d="M481 303 A62 40 0 0 1 540 270 L540 278 A55 34 0 0 0 493 303 Z"/></svg>
  <span class="page-no">6</span>
</section>

<!-- 7 Three columns -->
<section class="slide" style="left:51px;top:1575px">
  <h2 class="slide-title">Slide Title Goes Here</h2>
  <p class="slide-sub">Subtitle of Slide Goes Here</p>
  <div class="photo" role="img" aria-label="Photo of a business handshake" style="left:26px;top:90px;width:156px;height:75px;background:linear-gradient(135deg,#d9dde3,#9aa1ab)"></div>
  <div class="photo" role="img" aria-label="Photo of a tablet with a financial chart" style="left:192px;top:90px;width:156px;height:75px;background:linear-gradient(135deg,#e2e5ea,#5b636e)"></div>
  <div class="photo" role="img" aria-label="Photo of a team reviewing printed charts on a table" style="left:358px;top:90px;width:156px;height:75px;background:linear-gradient(135deg,#b89a86,#e8e4df)"></div>
  <div style="position:absolute;left:29px;top:173px;width:150px"><p class="item-title" style="font-size:10px">Title Goes Here</p><ul class="bullets" style="margin-top:6px"><li>Lorem ipsum dolor sit amet, consectetur adipiscing elit. Vivamus eu dui ex.</li><li>Curabitur dapibus dignissim dui, in molestie metus feugiat sed.</li><li>Praesent aliquet lorem ex, eu dapibus odio varius at.</li></ul></div>
  <div style="position:absolute;left:199px;top:173px;width:150px"><p class="item-title" style="font-size:10px">Title Goes Here</p><ul class="bullets" style="margin-top:6px"><li>Lorem ipsum dolor sit amet, consectetur adipiscing elit. Vivamus eu dui ex.</li><li>Curabitur dapibus dignissim dui, in molestie metus feugiat sed.</li><li>Praesent aliquet lorem ex, eu dapibus odio varius at.</li></ul></div>
  <div style="position:absolute;left:362px;top:173px;width:150px"><p class="item-title" style="font-size:10px">Title Goes Here</p><ul class="bullets" style="margin-top:6px"><li>Lorem ipsum dolor sit amet, consectetur adipiscing elit. Vivamus eu dui ex.</li><li>Curabitur dapibus dignissim dui, in molestie metus feugiat sed.</li><li>Praesent aliquet lorem ex, eu dapibus odio varius at.</li></ul></div>
  <div class="bar-footer"></div>
  <p class="logo logo--footer">MERIDEL</p>
  <svg class="page-arc" viewBox="0 0 540 303"><path d="M481 303 A62 40 0 0 1 540 270 L540 278 A55 34 0 0 0 493 303 Z"/></svg>
  <span class="page-no">7</span>
</section>

<!-- 8 Section break -->
<section class="slide" style="left:609px;top:1575px">
  <div class="fill" style="background:linear-gradient(90deg,#6f9fd9,#86afe0)"></div>
  <div class="photo" role="img" aria-label="Photo of hands reviewing documents and a laptop, blue tinted" style="left:340px;top:0;width:200px;height:303px;background:linear-gradient(180deg,#b7cce8,#9ab8df);opacity:.7"></div>
  <svg class="crescent" viewBox="0 0 540 303" style="height:303px"><path d="M380 0 A215 215 0 0 0 470 320 A240 240 0 0 1 340 0 Z"/></svg>
  <p class="logo" style="left:45px;top:87px;font-size:15px">PROJECT MERIDEL</p>
  <h2 class="cover-title" style="top:140px;font-size:27px;line-height:30px">Section Break<br>Goes Here!</h2>
  <p class="cover-sub" style="top:206px;font-size:12.5px">Subtitle of Section Break</p>
</section>

<!-- 9 Chart -->
<section class="slide" style="left:51px;top:1897px">
  <h2 class="slide-title">Slide Title Goes Here</h2>
  <p class="slide-sub">Subtitle of Slide Goes Here</p>
  <svg style="position:absolute;left:38px;top:88px" width="270" height="165" viewBox="0 0 270 165" font-family="Montserrat, Arial, sans-serif" font-size="5" fill="#555">
    <g stroke="#e3e3e3" stroke-width=".6">
      <line x1="14" y1="10" x2="262" y2="10"/><line x1="14" y1="30.5" x2="262" y2="30.5"/><line x1="14" y1="51" x2="262" y2="51"/><line x1="14" y1="71.5" x2="262" y2="71.5"/><line x1="14" y1="92" x2="262" y2="92"/><line x1="14" y1="112.5" x2="262" y2="112.5"/><line x1="14" y1="133" x2="262" y2="133"/>
    </g>
    <text x="6" y="12">6</text><text x="6" y="32.5">5</text><text x="6" y="53">4</text><text x="6" y="73.5">3</text><text x="6" y="94">2</text><text x="6" y="114.5">1</text><text x="6" y="135">0</text>
    <g fill="#0054AA"><rect x="39" y="51" width="9" height="82"/><rect x="100" y="50" width="9" height="83"/><rect x="161" y="61" width="9" height="72"/><rect x="222" y="40" width="9" height="93"/></g>
    <g fill="#0677BA"><rect x="52" y="84" width="9" height="49"/><rect x="113" y="82" width="9" height="51"/><rect x="174" y="96" width="9" height="37"/><rect x="235" y="76" width="9" height="57"/></g>
    <g fill="#7BADD7"><rect x="65" y="92" width="9" height="41"/><rect x="126" y="92" width="9" height="41"/><rect x="187" y="72" width="9" height="61"/><rect x="248" y="30" width="9" height="103"/></g>
    <g fill="#0677BA" text-anchor="middle"><text x="56" y="142">Category 1</text><text x="117" y="142">Category 2</text><text x="178" y="142">Category 3</text><text x="240" y="142">Category 4</text></g>
    <rect x="104" y="150" width="3" height="3" fill="#0054AA"/><text x="109" y="153" fill="#0677BA">Series 1</text>
    <rect x="134" y="150" width="3" height="3" fill="#0677BA"/><text x="139" y="153" fill="#0677BA">Series 2</text>
    <rect x="164" y="150" width="3" height="3" fill="#7BADD7"/><text x="169" y="153" fill="#0677BA">Series 3</text>
  </svg>
  <div class="legend-item" style="top:98px"><p class="item-title">Title Goes Here</p><p class="small">Lorem ipsum dolor sit amet, consectetur adipiscing elit. Vivamus eu dui ex. Curabitur dapibus dignissim dui, in molestie metus.</p></div>
  <div class="legend-item" style="top:151px"><p class="item-title" style="--c:0">Title Goes Here</p><p class="small">Lorem ipsum dolor sit amet, consectetur adipiscing elit. Vivamus eu dui ex. Curabitur dapibus dignissim dui, in molestie metus.</p></div>
  <div class="legend-item legend-item--soft" style="top:204px"><p class="item-title" style="color:var(--soft)">Title Goes Here</p><p class="small">Lorem ipsum dolor sit amet, consectetur adipiscing elit. Vivamus eu dui ex. Curabitur dapibus dignissim dui, in molestie metus.</p></div>
  <div class="bar-footer"></div>
  <p class="logo logo--footer">MERIDEL</p>
  <svg class="page-arc" viewBox="0 0 540 303"><path d="M481 303 A62 40 0 0 1 540 270 L540 278 A55 34 0 0 0 493 303 Z"/></svg>
  <span class="page-no">9</span>
</section>

<!-- 10 Table -->
<section class="slide" style="left:609px;top:1897px">
  <h2 class="slide-title">Slide Title Goes Here</h2>
  <p class="slide-sub">Subtitle of Slide Goes Here</p>
  <table class="grid-table">
    <thead><tr><th>Koptekst</th><th>Koptekst</th><th>Koptekst</th><th>Koptekst</th></tr></thead>
    <tbody>
      <tr><td>Tekst komt hier</td><td>Tekst komt hier</td><td>Tekst komt hier</td><td>Tekst komt hier</td></tr>
      <tr><td>Tekst komt hier</td><td>Tekst komt hier</td><td>Tekst komt hier</td><td>Tekst komt hier</td></tr>
      <tr><td>Tekst komt hier</td><td>Tekst komt hier</td><td>Tekst komt hier</td><td>Tekst komt hier</td></tr>
      <tr><td>Tekst komt hier</td><td>Tekst komt hier</td><td>Tekst komt hier</td><td>Tekst komt hier</td></tr>
      <tr><td>Tekst komt hier</td><td>Tekst komt hier</td><td>Tekst komt hier</td><td>Tekst komt hier</td></tr>
      <tr><td>Tekst komt hier</td><td>Tekst komt hier</td><td>Tekst komt hier</td><td>Tekst komt hier</td></tr>
      <tr><td>Tekst komt hier</td><td>Tekst komt hier</td><td>Tekst komt hier</td><td>Tekst komt hier</td></tr>
      <tr><td>Tekst komt hier</td><td>Tekst komt hier</td><td>Tekst komt hier</td><td>Tekst komt hier</td></tr>
      <tr><td>Tekst komt hier</td><td>Tekst komt hier</td><td>Tekst komt hier</td><td>Tekst komt hier</td></tr>
    </tbody>
  </table>
  <div class="bar-footer"></div>
  <p class="logo logo--footer">MERIDEL</p>
  <svg class="page-arc" viewBox="0 0 540 303"><path d="M481 303 A62 40 0 0 1 540 270 L540 278 A55 34 0 0 0 493 303 Z"/></svg>
  <span class="page-no">10</span>
</section>

<!-- 11 Contact -->
<section class="slide cover--dark" style="left:330px;top:2218px">
  <div class="fill"></div>
  <div class="photo photo--right" role="img" aria-label="Dark photo of a handshake across a desk" style="background:linear-gradient(180deg,#1c2536,#2c384f)"></div>
  <svg class="crescent" viewBox="0 0 540 282"><path d="M335 0 A200 200 0 0 0 505 285 A235 235 0 0 1 295 0 Z"/></svg>
  <p class="logo" style="left:45px;top:128px;font-size:15px">PROJECT MERIDEL</p>
  <p class="contact-head">Contact Us</p>
  <ul class="contact-list">
    <li><svg viewBox="0 0 10 10"><path d="M2 1 L4 3 L3 4.2 Q4.5 6 5.8 7 L7 6 L9 8 L7.8 9.2 Q4 8.5 0.8 2.2 Z" fill="#fff" stroke="none"/></svg>555-0134-2290</li>
    <li><svg viewBox="0 0 10 10"><circle cx="5" cy="5" r="1.8"/><path d="M6.8 5 Q6.8 7 8.2 6.8 Q9.2 6.4 9 5 A4 4 0 1 0 7 8.5"/></svg>info@project-meridel.com</li>
    <li><svg viewBox="0 0 10 10"><circle cx="5" cy="5" r="4"/><ellipse cx="5" cy="5" rx="1.8" ry="4"/><line x1="1" y1="5" x2="9" y2="5"/></svg>www.project-meridel.com</li>
  </ul>
  <footer class="legal">© 2020 <span>Project-Meridel</span> | All Rights Reserved.</footer>
</section>

</body>
</html>
```